Real estate investor, needing a business card that communicates warmth, integrity, empathy.

I have a logo that can be manipulated to align with the message - "Serving your home selling needs." Want it to stand out from typical real estate investor cards, and make distressed home sellers feel a connection with me. Should communicate warmth, integrity, empathy, and trustworthiness.

Target Market(s)

Distressed home owners who need to sell their homes, not using realtors.

Contact Information for Business Card

Glossy front and matte back, with a small box that is labelled "notes." I like darker blues and blacks together, but doesn't have to be, as long as it communicates trustworthiness, and a strong call to action.

Other font styles liked:
• see "must haves" above, but willing to review whatever comes my way.

Requirements
Must have
• The fonts on my logo are Aviano, Lusitana, and Marcellus. We don't have to use those, but I favor them.

```html
<!DOCTYPE html>
<html lang="en">
<head>
<meta charset="utf-8">
<title>Harbor Lane Homes – Business Card</title>
<link rel="stylesheet" href="https://fonts.googleapis.com/css2?family=Lusitana:wght@700&family=Roboto:wght@300;400;500&display=swap">
<style>
  :root {
    --stage: #474747;
    --card-white: #ffffff;
    --card-black: #0b0b0c;
    --band: #151516;
    --ink: #1c1c1c;
    --ink-soft: #3a3a3a;
    --accent-blue: #1f74c4;
    --on-dark: #ffffff;
    --on-dark-soft: #d8d8d8;
  }
  * { box-sizing: border-box; margin: 0; padding: 0; }
  html, body { width: 1200px; height: 876px; overflow: hidden; }
  body {
    background: var(--stage);
    font-family: "Roboto", Arial, sans-serif;
    position: relative;
  }
  .card {
    position: absolute;
    top: 288px;
    width: 525px;
    height: 300px;
    overflow: hidden;
  }
  .card--front { left: 45px; background: var(--card-white); }
  .card--back  { left: 630px; background: var(--card-black); }

  .wordmark {
    font-family: "Lusitana", Georgia, serif;
    font-weight: 700;
    letter-spacing: 0.04em;
  }
  .card--front .wordmark {
    position: absolute;
    left: 38px;
    top: 34px;
    font-size: 24px;
    color: var(--ink);
  }

  .contact-list {
    position: absolute;
    left: 38px;
    top: 92px;
    list-style: none;
    font-size: 13px;
    color: var(--ink-soft);
    line-height: 1.75;
  }
  .contact-list li { display: flex; align-items: center; gap: 8px; }
  .contact-list svg { width: 11px; height: 11px; flex: none; }
  .contact-list .web { color: var(--ink-soft); }
  .contact-list .web span { color: var(--accent-blue); }

  .person {
    position: absolute;
    right: 44px;
    top: 112px;
    text-align: right;
  }
  .person__name {
    font-size: 26px;
    font-weight: 500;
    color: var(--accent-blue);
  }
  .person__role {
    font-size: 15px;
    font-weight: 300;
    color: var(--ink-soft);
    margin-top: 2px;
  }

  .address-band {
    position: absolute;
    left: 0;
    bottom: 0;
    width: 330px;
    height: 36px;
    background: var(--band);
    clip-path: polygon(0 0, 100% 0, 92% 100%, 0 100%);
    color: var(--on-dark);
    font-size: 13px;
    font-weight: 300;
    display: flex;
    align-items: center;
    padding-left: 38px;
  }

  .card--back {
    display: flex;
    flex-direction: column;
    align-items: center;
    justify-content: center;
    background: linear-gradient(135deg, #1a1a1b 0%, var(--card-black) 55%, #050505 100%);
  }
  .card--back .wordmark {
    font-size: 36px;
    color: var(--on-dark);
  }
  .tagline {
    margin-top: 14px;
    font-size: 14px;
    font-weight: 300;
    color: var(--on-dark-soft);
    letter-spacing: 0.02em;
  }
</style>
</head>
<body>

  <section class="card card--front" aria-label="Business card front">
    <div class="wordmark">Harbor Lane Homes</div>

    <ul class="contact-list">
      <li>
        <svg viewBox="0 0 12 12" aria-hidden="true"><path d="M3 1l2 2.5-1.2 1.2a7 7 0 0 0 3.5 3.5L8.5 7 11 9l-1.3 1.8C5.5 11 1 6.5 1.2 2.3z" fill="var(--accent-blue)"/></svg>
        555-014-2276
      </li>
      <li>
        <svg viewBox="0 0 12 12" aria-hidden="true"><rect x="1" y="2.5" width="10" height="7" fill="none" stroke="var(--accent-blue)" stroke-width="1.2"/><path d="M1 2.5l5 4 5-4" fill="none" stroke="var(--accent-blue)" stroke-width="1.2"/></svg>
        hello@harborlanehomes.com
      </li>
      <li class="web">
        <svg viewBox="0 0 12 12" aria-hidden="true"><circle cx="6" cy="6" r="5" fill="var(--accent-blue)"/><path d="M1 6h10M6 1c-2.5 3-2.5 7 0 10M6 1c2.5 3 2.5 7 0 10" stroke="#fff" stroke-width="0.8" fill="none"/></svg>
        www.<span>harborlanehomes</span>.com
      </li>
    </ul>

    <div class="person">
      <div class="person__name">Daniel Reyes</div>
      <div class="person__role">Manager</div>
    </div>

    <div class="address-band">48 Alder Street, Portland, OR 97201</div>
  </section>

  <section class="card card--back" aria-label="Business card back">
    <div class="wordmark">Harbor Lane Homes</div>
    <p class="tagline">Serving your home selling needs</p>
  </section>

</body>
</html>
```